KV Group

We need a new website for our company and since we had a very good work done for our logo in this site, we're back for the entire job.

Our company name is Marlowe Capital Group. We're adding files of examples of what we have done today. In my opinion we need a more attention lock in the site but yet financial simple work.

Our files (attached) will let you know what we have so far. We need a complete change but the colours should be the same, however you can change them not running away to far from the original, and of course matching with the logo.

We need examples for 3 kind of layouts.

- A HOME welcome layout
- An internal Layout with sidebar
- And internal Layout wide

We can buy image licenses if needed for assets.
Actually there are 5 slide images placed on the Welcome HOME, we need those there, but you can improve with better images to match the new website!!!

Target Market(s)

Clients looking for financial advisers, tax and funds specialist, currency advisers

Industry/Entity Type

Financial

Requirements
Must have
• all the fonts must be in accordance with the financial market sites........the welcome home page must be precise, neat and information accurate........the menu should be elegant........main focus on the Home page, should be also the PRIVATE ACCESS box log in.......

```html
<!DOCTYPE html>
<html lang="en">
<head>
<meta charset="utf-8">
<title>Marlowe Capital Group</title>
<link href="https://fonts.googleapis.com/css2?family=Dosis:wght@500;600&family=Oswald:wght@500;600&family=PT+Sans:wght@400;700&display=swap" rel="stylesheet">
<style>
:root{
  --page:#efebe4;
  --panel:#f8f6f1;
  --brown:#4a2b10;
  --brown-dark:#3a220c;
  --orange:#e8761c;
  --ink:#2e2a26;
  --muted:#5a544d;
  --rule:#cfc8bc;
  --footer:#3e3e3e;
  --footer-base:#333333;
  --footer-text:#e6e2dc;
  --up:#2c8a2c;
  --down:#c0261e;
}
*{box-sizing:border-box;margin:0;padding:0}
html,body{width:847px;height:1200px;overflow:hidden}
body{background:var(--page);font-family:"PT Sans",Arial,sans-serif;color:var(--ink);position:relative}
.abs{position:absolute}

.utility-tab{left:602px;top:0;width:170px;height:29px;background:var(--brown-dark);border-radius:0 0 5px 5px;display:flex;align-items:center;justify-content:space-around;color:#fff;font-size:12px}
.utility-tab span{display:flex;align-items:center;gap:5px}

.brand{left:73px;top:20px;display:flex;align-items:center;gap:8px}
.brand-mark{width:30px;height:30px;background:var(--orange)}
.brand-name{font-family:"Dosis",sans-serif;font-weight:600;font-size:17px;color:var(--ink);letter-spacing:.5px}

.main-nav{left:293px;top:52px;width:479px;height:23px;display:flex;align-items:center;justify-content:space-between;font-family:"Dosis",sans-serif;font-weight:500;font-size:13px;color:var(--ink)}
.main-nav .active{background:var(--orange);color:#fff;padding:3px 13px}
.main-nav .sep{width:1px;height:11px;background:#888}
.header-rule{left:73px;top:88px;width:699px;height:1px;background:var(--rule)}

.hero{left:73px;top:103px;width:699px;height:313px;background:linear-gradient(120deg,#e9e4dc 0%,#b8a791 35%,#6b5a47 70%,#3a2d21 100%);overflow:hidden}
.hero-copy{left:133px;top:244px;font-family:"Oswald",sans-serif;font-weight:600;color:#fff;line-height:1}
.hero-copy .l1{font-size:42px;letter-spacing:1px}
.hero-copy .l2{font-size:68px;color:#3a250f;margin-top:0;letter-spacing:2px;margin-left:-4px}
.hero-copy .l3{font-size:31px;color:#2b1b0b;margin-top:4px;letter-spacing:2px}
.slide-btn{top:240px;width:36px;height:36px;border-radius:50%;background:rgba(255,255,255,.45);display:flex;align-items:center;justify-content:center}

.ticker{left:73px;top:431px;width:699px;height:29px;background:#fff;border:1px solid var(--rule);display:flex;align-items:center;justify-content:space-between;padding:0 6px;font-size:7.5px;font-weight:700}
.ticker .up{color:var(--up)} .ticker .down{color:var(--down)}

.about{left:73px;top:475px;width:699px;height:136px;background:var(--panel);padding:10px 17px}
.section-title{display:flex;align-items:center;gap:10px;font-family:"Dosis",sans-serif;font-weight:500;font-size:18px;color:var(--ink)}
.section-title::before,.section-title::after{content:"";flex:1;height:1px;background:var(--rule)}
.about p{font-size:9.6px;line-height:1.3;color:var(--muted);margin-top:6px}
.read-more{background:var(--brown);color:#fff;font-family:"Dosis",sans-serif;font-size:13px;padding:3px 15px;display:inline-block}
.about-cta{display:flex;align-items:center;gap:10px;margin-top:5px}
.about-cta::before,.about-cta::after{content:"";flex:1;height:1px;background:var(--rule)}

.feature{top:630px;width:160px}
.feature h3{font-family:"Dosis",sans-serif;font-weight:500;font-size:15px;color:var(--ink);height:29px}
.feature .photo{width:160px;height:97px}
.feature p{font-size:8.6px;line-height:1.35;color:var(--muted);margin-top:8px}

.login{left:612px;top:659px;width:160px;height:151px;background:var(--brown);padding:10px 10px;color:#fff;font-size:9.5px}
.login label{display:block;margin-bottom:3px}
.login .field{height:23px;background:#fff;margin-bottom:9px}
.login .row{display:flex;justify-content:space-between;align-items:flex-start}
.login .read-more{background:#2c1a08;font-size:11px;padding:2px 10px;margin-top:12px}

.trust{left:73px;top:836px;width:699px;height:91px;background:var(--panel);padding:7px 10px}
.trust-inner{background:#fff;height:77px;display:flex;align-items:center;border:1px solid #e4dfd6}
.trust-label{width:120px;text-align:center;font-family:"Dosis",sans-serif;font-weight:600;font-size:15px;line-height:1.3;border-right:1px solid var(--rule)}
.badges{flex:1;display:flex;align-items:center;justify-content:space-around;padding:0 30px}

.site-footer{left:0;top:947px;width:847px;height:203px;background:var(--footer)}
.foot-col{top:956px;color:var(--footer-text);font-size:9.5px;line-height:14px}
.foot-col h4{font-family:"Dosis",sans-serif;font-weight:500;font-size:17px;color:var(--orange);margin-bottom:9px;line-height:20px}
.footer-base{left:0;top:1150px;width:847px;height:50px;background:var(--footer-base);display:flex;align-items:center;justify-content:space-between;padding:0 75px;color:#8a8783;font-size:8px}
.footer-base span{white-space:nowrap}
.footer-base p{width:480px;line-height:1.3;color:#6e6b67}
</style>
</head>
<body>

<div class="abs utility-tab">
  <span><svg width="14" height="12" viewBox="0 0 14 12"><path d="M1 6l4 4 8-9" stroke="#fff" stroke-width="2" fill="none"/></svg>Apply Now</span>
  <span><svg width="14" height="10" viewBox="0 0 14 10"><rect x="0.5" y="0.5" width="13" height="9" fill="none" stroke="#fff"/><path d="M1 1l6 5 6-5" stroke="#fff" fill="none"/></svg>Contact us</span>
</div>

<div class="abs brand"><div class="brand-mark"></div><div class="brand-name">MARLOWE CAPITAL GROUP</div></div>

<nav class="abs main-nav">
  <span class="active">Home</span><span class="sep"></span><span>About us</span><span class="sep"></span><span>Investments</span><span class="sep"></span><span>Funds</span><span class="sep"></span><span>Brokerage</span><span class="sep"></span><span>Exchange</span><span class="sep"></span><span>Accounts</span>
</nav>
<div class="abs header-rule"></div>

<div class="abs hero" role="img" aria-label="Sepia photo of business advisers working together over documents"></div>
<div class="abs hero-copy">
  <div class="l1">TEAMWORK FOR</div>
  <div class="l2">YOUR BENEFIT</div>
  <div class="l3">NORTHGATE ONLINE</div>
</div>
<div class="abs slide-btn" style="left:80px"><svg width="12" height="14"><path d="M9 1L3 7l6 6" stroke="#fff" stroke-width="2.5" fill="none"/></svg></div>
<div class="abs slide-btn" style="left:729px"><svg width="12" height="14"><path d="M3 1l6 6-6 6" stroke="#fff" stroke-width="2.5" fill="none"/></svg></div>

<div class="abs ticker">
  <span>GBP/EUR = <span class="up">1.18682 ▲</span></span>
  <span>GBP/AUD = <span class="up">1.70182 ▲</span></span>
  <span>GBP/CAD = <span class="down">1.62817 ▼</span></span>
  <span>GBP/USD = <span class="up">1.56322 ▲</span></span>
  <span>GBP/NZD = <span class="up">1.95402 ▲</span></span>
  <span>GBP/TRY = <span class="up">3.20381 ▲</span></span>
  <span>GBP/CAD = <span class="down">1.62817 ▼</span></span>
</div>

<section class="abs about">
  <h2 class="section-title">About Company</h2>
  <p>Lorem Ipsum is simply dummy text of the printing and typesetting industry. Lorem Ipsum has been the industry's standard dummy text ever since the 1500s, when an unknown printer took a galley of type and scrambled it to make a type specimen book. It has survived not only five centuries, but also the leap into electronic typesetting, remaining essentially unchanged. It was popularised in the 1960s with the release of Lettrex sheets containing Lorem Ipsum passages, and more recently with desktop publishing software like PageForge including versions of Lorem Ipsum.</p>
  <div class="about-cta"><span class="read-more">Read More</span></div>
</section>

<div class="abs feature" style="left:73px">
  <h3>Management &amp; Stratery</h3>
  <div class="photo" role="img" aria-label="Hands with a pen over printed financial charts" style="background:linear-gradient(135deg,#f4f4f2,#d9dcd6 50%,#a9c86a)"></div>
  <p>Lorem Ipsum is simply dummy text of the printing and typesetting industry. Lorem Ipsum has been the industry's standard dummy text ever since the 1500s</p>
</div>
<div class="abs feature" style="left:252px">
  <h3>Funds</h3>
  <div class="photo" role="img" aria-label="Business team shaking hands in an office" style="background:linear-gradient(135deg,#e8e6e2,#9a8d80 55%,#3d3a3a)"></div>
  <p>Lorem Ipsum is simply dummy text of the printing and typesetting industry. Lorem Ipsum has been the industry's standard dummy text ever since the 1500s</p>
</div>
<div class="abs feature" style="left:431px">
  <h3>Currency Exchange</h3>
  <div class="photo" role="img" aria-label="Glass office towers against a blue sky" style="background:linear-gradient(180deg,#bcd6ee,#5f8fb8 60%,#4f7a3a)"></div>
  <p>Lorem Ipsum is simply dummy text of the printing and typesetting industry. Lorem Ipsum has been the industry's standard dummy text ever since the 1500s</p>
</div>
<div class="abs feature" style="left:612px"><h3>Private Access</h3></div>

<form class="abs login">
  <label>User Name:</label><div class="field"></div>
  <label>Password:</label><div class="field"></div>
  <div class="row"><span>Forgot password</span></div>
  <div class="row" style="justify-content:flex-end"><span class="read-more">Read More</span></div>
</form>

<section class="abs trust">
  <div class="trust-inner">
    <div class="trust-label">Verified<br>and<br>Protected by</div>
    <div class="badges">
      <svg width="80" height="40"><ellipse cx="40" cy="20" rx="38" ry="18" fill="none" stroke="#8a1c2c" stroke-width="2"/></svg>
      <svg width="84" height="34"><rect width="84" height="34" fill="#1b3f8f"/></svg>
      <svg width="97" height="28"><rect width="97" height="28" rx="4" fill="#7ab33a"/></svg>
      <svg width="54" height="54"><circle cx="27" cy="27" r="25" fill="#1e2e6e" stroke="#e8761c" stroke-width="3"/></svg>
    </div>
  </div>
</section>

<footer class="abs site-footer"></footer>
<div class="abs foot-col" style="left:73px"><h4>About us</h4>History<br>Expertize<br>Identity<br>Strategy<br>Contact us</div>
<div class="abs foot-col" style="left:196px"><h4>Investments</h4>Term Deposits<br>management &amp; Strategy<br>Client Relations<br>Financial Privacy<br>Tax Advice<br>Wealth Analysis &amp; Financial Planning<br>Active Advisory Group<br>Manager Selection Services<br>Private Equity</div>
<div class="abs foot-col" style="left:363px"><h4>Currency Exchange</h4>Overview<br>Administration<br>Funds Security<br>Core Services<br>Reporting<br>Revenue oprtunities<br>How it works?<br>Glossary</div>
<div class="abs foot-col" style="left:506px"><h4>Funds</h4>Foreign Exchange<br>Fx Forward<br>Fx Options<br><h4 style="margin-top:19px">Brokerage</h4>Institutional<br>Research<br>Trading</div>
<div class="abs foot-col" style="left:650px"><h4>Accounts</h4>Apply Now<br>Private Access</div>

<div class="abs footer-base">
  <span>© Copyright websitename . All Rights Reserved</span>
  <p>Our advisers bring decades of experience in wealth management, currency exchange and fund selection. We combine careful research with personal service so every client can plan ahead with confidence. Your goals stay at the centre of each decision we make, from first meeting to long term review and reporting.</p>
</div>

</body>
</html>
```